Banner design

Hello.
I require a top header banner for my Interactive and electronic whiteboard / Audio Visual business.
Animated gif.

http://www.qorvantix.com.au

Basically a few photos, my phone number and my new logo (coming soon "Palquestron")
Corporate looking, that immediately captures the customers attention.

Target Market(s)

Adults in Western speaking country (Australia). To young business professionals, teachers, managers etc

Industry/Entity Type

Electronic

```html
<!DOCTYPE html>
<html lang="en">
<head>
<meta charset="utf-8">
<title>Qorvantix – Hire, Sales, Services</title>
<link href="https://fonts.googleapis.com/css2?family=Arimo:wght@700&family=Raleway:wght@200;500&display=swap" rel="stylesheet">
<style>
  :root{
    --frame-outer:#0a1a26;
    --frame-line:#cfe6f2;
    --deep:#041b2c;
    --mid:#0b4a6e;
    --glow:#3fa6cf;
    --text:#ffffff;
    --domain:rgba(255,255,255,0.55);
    --icon-ring:#e9f6fb;
  }
  html,body{margin:0;padding:0;overflow:hidden;background:var(--frame-outer);}
  .banner{
    position:relative;width:1200px;height:318px;box-sizing:border-box;
    border:3px solid var(--frame-outer);overflow:hidden;
    background:
      radial-gradient(ellipse 420px 260px at 560px 130px, rgba(110,200,235,0.55), transparent 70%),
      linear-gradient(90deg, var(--deep) 0%, var(--mid) 35%, #0e5f86 50%, var(--mid) 70%, var(--deep) 100%);
  }
  .banner::after{
    content:"";position:absolute;inset:2px;border:1px solid var(--frame-line);opacity:.5;pointer-events:none;
  }
  .photo-team{
    position:absolute;left:0;top:0;width:300px;height:318px;
    background:linear-gradient(90deg,#1c2a36 0%,#2e4252 45%,#35607a 75%,rgba(11,74,110,0) 100%);
  }
  .photo-laptop{
    position:absolute;right:0;top:0;width:320px;height:318px;
    background:linear-gradient(270deg,#0d1a24 0%,#1f5d86 30%,#2c86b5 55%,rgba(11,74,110,0) 100%);
  }
  .offer-list{
    position:absolute;left:398px;top:38px;margin:0;padding:0;list-style:none;
    font-family:"Raleway",sans-serif;font-weight:500;color:var(--text);
    font-size:38px;letter-spacing:.42em;line-height:55px;
  }
  .offer-list li{display:flex;align-items:center;}
  .offer-list svg{width:28px;height:28px;margin-right:14px;flex:none;}
  .phone{
    position:absolute;left:230px;top:230px;margin:0;
    font-family:"Arimo",sans-serif;font-weight:700;font-variant:small-caps;
    font-size:38px;color:var(--text);letter-spacing:.01em;
    text-shadow:0 2px 4px rgba(0,0,0,.6);white-space:nowrap;
  }
  .domain{
    position:absolute;left:222px;top:278px;margin:0;
    font-family:"Raleway",sans-serif;font-weight:200;font-size:44px;
    letter-spacing:.62em;color:var(--domain);white-space:nowrap;
  }
</style>
</head>
<body>
  <div class="banner">
    <div class="photo-team" role="img" aria-label="Two businessmen in suits looking at a laptop"></div>
    <div class="photo-laptop" role="img" aria-label="Laptop with a desktop screen and a glowing data trail"></div>

    <ul class="offer-list">
      <li><svg viewBox="0 0 28 28" aria-hidden="true"><circle cx="14" cy="14" r="12" fill="#0b3550" stroke="var(--icon-ring)" stroke-width="2"/><path d="M14 8v12M8 14h12" stroke="var(--icon-ring)" stroke-width="3"/></svg>Hire</li>
      <li><svg viewBox="0 0 28 28" aria-hidden="true"><circle cx="14" cy="14" r="12" fill="#0b3550" stroke="var(--icon-ring)" stroke-width="2"/><path d="M14 8v12M8 14h12" stroke="var(--icon-ring)" stroke-width="3"/></svg>Sales</li>
      <li><svg viewBox="0 0 28 28" aria-hidden="true"><circle cx="14" cy="14" r="12" fill="#0b3550" stroke="var(--icon-ring)" stroke-width="2"/><path d="M14 8v12M8 14h12" stroke="var(--icon-ring)" stroke-width="3"/></svg>Services</li>
    </ul>

    <p class="phone">Phone: 0400 555 128 or (02) 5550 1947</p>
    <p class="domain">qorvantix.com</p>
  </div>
</body>
</html>
```